K Forgeworks Design and Analytics
Tech Consulting Company
K Forgeworks Design and Analytics - Information Technology
Creative Brief
Simple
Marcus Pellham
President/CEO
748 South Quillon Ave Baltimore, MD 21287
m.pellham@kfda-mail.com
Just the Logo on the back

```html
<!DOCTYPE html>
<html lang="en">
<head>
<meta charset="utf-8">
<title>K Forgeworks Design and Analytics – Stationery Set</title>
<link href="https://fonts.googleapis.com/css2?family=Montserrat:wght@400;600;800&family=Great+Vibes&display=swap" rel="stylesheet">
<style>
:root{
  --backdrop:#7b7b7b;
  --ink:#111111;
  --paper:#ffffff;
  --mid:#8a8a8a;
  --soft:#d6d6d6;
  --dark-panel:#1c1c1c;
  --shade:#2e2e2e;
}
*{box-sizing:border-box;margin:0;padding:0}
html,body{width:1200px;height:430px;overflow:hidden}
body{background:var(--backdrop);font-family:"Montserrat",Arial,sans-serif;color:var(--ink);position:relative}
.item{position:absolute;box-shadow:0 1px 3px rgba(0,0,0,.35)}
.wordmark{font-weight:800;letter-spacing:.08em;line-height:1}
.tagline{font-size:3px;letter-spacing:.06em;font-weight:400;margin-top:1px}
.paper{background:var(--paper);color:var(--ink)}
.black{background:var(--ink);color:var(--paper)}

/* business cards */
.card{width:106px;height:50px;padding:7px}
.card .wordmark{font-size:12px}
.card-back{display:flex;flex-direction:column;align-items:center;justify-content:center}
.card-front .name{font-size:5px;font-weight:600;margin-top:6px}
.card-front .role{font-size:3.5px}
.card-front .contact{font-size:3px;line-height:1.35;margin-top:3px}
.card-band{position:absolute;left:0;right:0;bottom:0;height:8px;background:var(--ink)}

/* letterhead */
.letterhead{left:165px;top:28px;width:190px;height:392px;padding:14px 16px}
.letterhead .wordmark{font-size:17px}
.letter-body{font-size:4px;line-height:1.6;margin-top:20px;color:#333}
.letter-body p{margin-bottom:6px}
.signature{font-family:"Great Vibes",cursive;font-size:15px;margin:8px 0 2px}
.letter-footer{position:absolute;left:0;right:0;bottom:16px;height:20px;background:var(--ink);color:var(--paper);font-size:3.5px;display:flex;align-items:center;justify-content:space-around}

/* fax sheet */
.fax{left:358px;top:90px;width:132px;height:330px;padding:14px 12px}
.fax .wordmark{font-size:14px}
.fax-title{position:absolute;right:12px;top:44px;font-size:12px;font-weight:800;letter-spacing:.1em}
.fax-fields{margin-top:48px;font-size:4px}
.fax-fields div{border-bottom:.5px solid var(--mid);padding:4px 0}
.fax-footer{position:absolute;left:0;right:0;bottom:14px;height:14px;background:var(--ink)}

/* folder */
.folder-panel{top:24px;width:157px;height:190px;overflow:hidden}
.folder-panel .wordmark{font-size:20px;position:absolute;left:14px;top:16px}
.folder-panel .tagline{position:absolute;left:14px;top:38px;font-size:3.5px}
.folder-panel .web{position:absolute;right:12px;bottom:62px;font-size:4px}
.folder-panel svg{position:absolute;left:0;bottom:0}

/* cd and sleeve */
.cd{left:823px;top:10px;width:124px;height:124px;border-radius:50%;background:var(--paper);display:flex;align-items:center;justify-content:center}
.cd::after{content:"";position:absolute;left:50%;top:50%;width:24px;height:24px;margin:-12px 0 0 -12px;border-radius:50%;background:var(--backdrop);box-shadow:inset 0 0 0 5px var(--soft)}
.cd .wordmark{font-size:14px;position:absolute;top:26px}
.sleeve{left:955px;top:20px;width:240px;height:136px;padding:14px}
.sleeve .wordmark{font-size:18px}
.sleeve .signature{position:absolute;right:18px;top:50px;font-size:14px}

/* presentation slides */
.slide{width:102px;height:74px;padding:6px;font-size:3.5px}
.slide-head{background:var(--ink);color:var(--paper);margin:-6px -6px 6px;padding:6px;font-size:5px;font-weight:800;letter-spacing:.05em}
.slide .wordmark{font-size:9px}
.slide ul{list-style:none;line-height:1.8}
.slide li::before{content:"";display:inline-block;width:3px;height:3px;background:var(--ink);margin-right:3px}
.thanks{display:flex;flex-direction:column;justify-content:center;padding-left:10px}
.thanks strong{font-size:7px;font-weight:800;line-height:1.2}

/* envelopes */
.envelope{width:200px;height:96px;padding:10px}
.envelope .wordmark{font-size:11px}
.envelope .tagline{font-size:3px}
.envelope-band{position:absolute;left:0;top:0;width:60px;height:8px;background:var(--ink)}
.clip{left:830px;top:240px;width:180px;height:14px;transform:rotate(8deg);border-radius:3px}
</style>
</head>
<body>

<!-- business cards -->
<div class="item card paper card-back" style="left:12px;top:95px">
  <div class="wordmark">KFDA</div>
  <div class="tagline">K Forgeworks Design and Analytics</div>
</div>
<div class="item card black card-front" style="left:12px;top:150px">
  <div class="wordmark">KFDA</div>
  <div class="name">Marcus Pellham</div>
  <div class="role">President/CEO</div>
</div>
<div class="item card paper card-front" style="left:12px;top:205px">
  <div class="wordmark">KFDA</div>
  <div class="contact">748 South Quillon Ave Baltimore, MD 21287<br>m.pellham@kfda-mail.com<br>kfda-mail.com</div>
</div>
<div class="item card black card-back" style="left:12px;top:260px">
  <div class="wordmark">KFDA</div>
  <div class="tagline">K Forgeworks Design and Analytics</div>
</div>
<div class="item card black card-back" style="left:12px;top:340px">
  <div class="wordmark">KFDA</div>
  <div class="tagline">K Forgeworks Design and Analytics</div>
</div>

<!-- letterhead -->
<div class="item paper letterhead">
  <div class="wordmark">KFDA</div>
  <div class="tagline" style="font-size:3.5px">K Forgeworks Design and Analytics</div>
  <div class="letter-body">
    <p>Project Office<br>Client Services<br>Baltimore, MD</p>
    <p>Dear Client,</p>
    <p>Thank you for your interest in our consulting services. We look forward to reviewing your requirements and outlining a plan.</p>
    <p>Our team will follow up with a detailed proposal and schedule within the coming week.</p>
    <p>Sincerely,</p>
    <div class="signature">Marcus Pellham</div>
    <p>Marcus Pellham<br>President/CEO</p>
  </div>
  <div class="letter-footer">
    <span>748 South Quillon Ave Baltimore, MD 21287</span>
    <span>kfda-mail.com</span>
  </div>
</div>

<div class="item card paper card-front" style="left:132px;top:345px;width:100px;height:46px">
  <div class="name" style="margin-top:0">Marcus Pellham</div>
  <div class="role">President/CEO</div>
  <div class="contact">m.pellham@kfda-mail.com</div>
  <div class="card-band"></div>
</div>

<!-- fax -->
<div class="item paper fax">
  <div class="wordmark">KFDA</div>
  <div class="tagline">K Forgeworks Design and Analyt</div>
  <div class="fax-title">FAX</div>
  <div class="fax-fields">
    <div>To:</div><div>From:</div><div>Date:</div><div>Pages:</div>
  </div>
  <div class="fax-footer"></div>
</div>

<!-- folder -->
<div class="item black folder-panel" style="left:492px">
  <div class="wordmark">KFDA</div>
  <div class="tagline">K Forgeworks Design and Analytics</div>
  <div class="web">kfda-mail.com</div>
  <svg width="157" height="60" viewBox="0 0 157 60"><polygon points="0,60 0,30 60,0 157,50 157,60" fill="var(--shade)"/><polygon points="60,0 100,60 20,60" fill="var(--mid)"/></svg>
</div>
<div class="item black folder-panel" style="left:655px">
  <div class="wordmark">KFDA</div>
  <div class="tagline">K Forgeworks Design and Analytics</div>
  <svg width="157" height="60" viewBox="0 0 157 60"><polygon points="0,60 90,10 157,40 157,60" fill="var(--shade)"/><polygon points="90,10 130,60 50,60" fill="var(--mid)"/></svg>
</div>

<!-- cd and sleeve -->
<div class="item cd"><div class="wordmark">KFDA</div></div>
<div class="item paper sleeve">
  <div class="wordmark">KFDA</div>
  <div class="tagline" style="font-size:3.5px">K Forgeworks Design and Analytics</div>
  <div class="signature">Marcus Pellham</div>
</div>

<!-- presentation slides -->
<div class="item paper slide" style="left:492px;top:222px">
  <div class="slide-head">PRESENTATION NAME</div>
  <div>Presenter name</div>
  <div class="wordmark" style="margin-top:14px">KFDA</div>
</div>
<div class="item paper slide" style="left:601px;top:222px">
  <div class="slide-head">Section Title</div>
  <ul><li>Key point one</li><li>Key point two</li><li>Key point three</li></ul>
</div>
<div class="item paper slide" style="left:710px;top:222px">
  <div class="slide-head">Results</div>
  <svg width="40" height="40" viewBox="0 0 40 40" style="margin-left:26px"><circle cx="20" cy="20" r="18" fill="var(--soft)"/><path d="M20 20 L20 2 A18 18 0 0 1 37 26 Z" fill="var(--ink)"/><path d="M20 20 L37 26 A18 18 0 0 1 12 36 Z" fill="var(--mid)"/></svg>
</div>
<div class="item paper slide" style="left:492px;top:304px">
  <div class="slide-head">Overview</div>
  <svg width="88" height="34" viewBox="0 0 88 34"><rect x="4" y="14" width="10" height="20" fill="var(--ink)"/><rect x="22" y="6" width="10" height="28" fill="var(--mid)"/><rect x="40" y="18" width="10" height="16" fill="var(--ink)"/><rect x="58" y="2" width="10" height="32" fill="var(--mid)"/></svg>
</div>
<div class="item paper slide" style="left:601px;top:304px">
  <div class="slide-head">Section Title</div>
  <ul><li>Key point one</li><li>Key point two</li></ul>
</div>
<div class="item black slide thanks" style="left:710px;top:304px">
  <strong>THANK YOU<br>SO MUCH</strong>
</div>

<!-- envelopes -->
<div class="item black clip"></div>
<div class="item paper envelope" style="left:830px;top:275px">
  <div class="envelope-band"></div>
  <div class="wordmark" style="margin-top:6px">KFDA</div>
  <div class="tagline">K Forgeworks Design and Analytics</div>
</div>
<div class="item paper envelope" style="left:990px;top:300px;width:205px;height:110px">
  <div class="envelope-band"></div>
  <div class="wordmark" style="margin-top:6px">KFDA</div>
  <div class="tagline">748 South Quillon Ave Baltimore, MD 21287</div>
</div>

</body>
</html>
```